Financial Planning Business needs a business card design

We need a business card design that is for a new financial planning business based in Australia. We provide financial planning advice such as retirement planning, wealth creation, asset protection.

Attached is the logo design. On the front side of the business card needs to incorporate the following:
- adviser name
- adviser title (ie Managing Director)
- address
- phone number
- email
- website address

Ideally it should also have the business name and logo

On the back of the card I would like this to be black in colour with the business name and logo

I have been advised the font is "Cinzel" (regular and bold)

Industry/Entity Type

Financial

Requirements
Must have
• Logo and business name

Format to have as follows:
Ben xxxxxxxx
Managing Director / Senior Financial Adviser
address
phone email
website

```html
<!DOCTYPE html>
<html lang="en">
<head>
<meta charset="utf-8">
<title>Keystone Wealth Planning – Business Card</title>
<link href="https://fonts.googleapis.com/css2?family=Exo+2:wght@400;600;700&display=swap" rel="stylesheet">
<style>
  :root {
    --backdrop: #8d8f91;
    --card-white: #ffffff;
    --card-grey: #e9eaeb;
    --brand-blue: #1aa3dc;
    --charcoal: #333536;
    --text-dark: #2e3031;
    --text-mid: #4a4c4e;
  }
  * { margin: 0; padding: 0; box-sizing: border-box; }
  html, body { width: 1200px; height: 894px; overflow: hidden; }
  body { background: var(--backdrop); position: relative; font-family: "Exo 2", sans-serif; }

  .card {
    position: absolute;
    overflow: hidden;
    box-shadow: 0 6px 18px rgba(0,0,0,0.25);
  }

  /* Shared wordmark: one font, one weight, one colour */
  .brand {
    display: flex; align-items: center; gap: 12px;
    font-family: "Exo 2", sans-serif; font-weight: 600;
    color: var(--brand-blue); white-space: nowrap;
  }
  .brand-mark { background: var(--brand-blue); flex: none; }
  .brand-name { line-height: 1; letter-spacing: 0.04em; }

  /* Back of card */
  .card-back {
    left: 580px; top: 70px; width: 560px; height: 320px;
    background: var(--card-white);
    display: flex; align-items: center; justify-content: center;
  }
  .card-back .brand-mark { width: 22px; height: 22px; }
  .card-back .brand-name { font-size: 26px; }

  /* Front of card */
  .card-front {
    left: 60px; top: 420px; width: 640px; height: 366px;
    background: linear-gradient(135deg, var(--card-white) 0%, var(--card-grey) 100%);
  }
  .card-front .brand { position: absolute; left: 34px; top: 40px; }
  .card-front .brand-mark { width: 18px; height: 18px; }
  .card-front .brand-name { font-size: 20px; }

  .band-dark {
    position: absolute; left: 0; top: 118px; width: 212px; height: 40px;
    background: var(--charcoal);
  }
  .band-blue {
    position: absolute; left: 222px; top: 132px; right: 0; height: 50px;
    background: var(--brand-blue);
    display: flex; align-items: center; padding-left: 62px;
    color: #fff; font-size: 15px; letter-spacing: 0.06em;
  }

  .adviser {
    position: absolute; left: 420px; top: 72px;
    color: var(--text-dark); text-transform: uppercase;
  }
  .adviser-name { font-size: 19px; font-weight: 700; letter-spacing: 0.08em; }
  .adviser-title { font-size: 11px; font-weight: 600; letter-spacing: 0.12em; margin-top: 2px; }

  .contact-list, .web-list { position: absolute; list-style: none; }
  .contact-list { left: 30px; top: 176px; }
  .web-list { left: 330px; top: 262px; }
  .contact-list li, .web-list li {
    display: flex; align-items: center; gap: 10px;
    font-size: 11px; color: var(--text-mid); letter-spacing: 0.04em;
    height: 22px;
  }
  .icon {
    width: 15px; height: 15px; background: var(--charcoal);
    display: flex; align-items: center; justify-content: center; flex: none;
  }
  .icon svg { width: 9px; height: 9px; }
</style>
</head>
<body>

  <section class="card card-back" aria-label="Card back">
    <div class="brand">
      <span class="brand-mark"></span>
      <span class="brand-name">KEYSTONE WEALTH PLANNING</span>
    </div>
  </section>

  <section class="card card-front" aria-label="Card front">
    <div class="brand">
      <span class="brand-mark"></span>
      <span class="brand-name">KEYSTONE WEALTH PLANNING</span>
    </div>

    <div class="adviser">
      <p class="adviser-name">Daniel Reeves</p>
      <p class="adviser-title">Manager</p>
    </div>

    <div class="band-dark"></div>
    <div class="band-blue">www.keystonewp.au/plan</div>

    <ul class="contact-list">
      <li><span class="icon"><svg viewBox="0 0 10 10"><path d="M5 0.5a3.2 3.2 0 0 0-3.2 3.2C1.8 6.2 5 9.5 5 9.5s3.2-3.3 3.2-5.8A3.2 3.2 0 0 0 5 0.5zm0 4.5a1.3 1.3 0 1 1 0-2.6 1.3 1.3 0 0 1 0 2.6z" fill="#fff"/></svg></span>14 Harbour Lane Sydney</li>
      <li><span class="icon"><svg viewBox="0 0 10 10"><path d="M2.2 0.8l1.6 1.9-0.9 1.2c0.6 1.3 1.6 2.3 2.9 2.9l1.2-0.9 1.9 1.6-0.8 1.5C4.6 8.8 1.2 5.4 0.7 1.6z" fill="#fff"/></svg></span>024 681 3579</li>
      <li><span class="icon"><svg viewBox="0 0 10 10"><rect x="0.8" y="2" width="8.4" height="6" fill="#fff"/><path d="M0.8 2l4.2 3.3L9.2 2" stroke="#333536" stroke-width="0.9" fill="none"/></svg></span>daniel@keystonewp.au</li>
    </ul>

    <ul class="web-list">
      <li><span class="icon"><svg viewBox="0 0 10 10"><circle cx="5" cy="5" r="3.8" stroke="#fff" stroke-width="0.9" fill="none"/><path d="M1.2 5h7.6M5 1.2c-1.6 2.3-1.6 5.3 0 7.6M5 1.2c1.6 2.3 1.6 5.3 0 7.6" stroke="#fff" stroke-width="0.7" fill="none"/></svg></span>www.keystonewp.au</li>
      <li><span class="icon"></span>news.keystonewp.au</li>
      <li><span class="icon"></span>social.keystonewp.au</li>
    </ul>
  </section>

</body>
</html>
```